Flyer for photo scanning business

Hello,
I need a flyer created for my business that would be suitable for print, to drop in letterboxes in my local community.

I would like the flyer to convey very simply the services I offer which is scanning negatives, slides and VHS tapes to digital files.
Hopefully it can make it look like an easy process, as people are often daunted by the task of sorting through old photos so they don't always get around to having them scanned.

I have a pinned facebook post that can be used by the designer to reference my services. Pricing does not need to be included on the flyer.
http://facebook.com/brightvaleimaging

Target Market(s)

Parents & Grandparents

Requirements
Must have
• Must make my services look simple! Refer to pinned facebook post for detailed outline of my services.

I would like to flyer to point towards my contact details -
www.brightvale.com
Margot 0478 219 836

Colours in line with my logo/brand (uploaded to brief).
Nice to have
• Stock images of 35mm film negatives, 8mm film, VHS tapes, or Lumavert slides would be worth including. I have also uploaded a mockup of the USB sticks that I provide with digitised images.
Should not have
• no prices needed,

```html
<!DOCTYPE html>
<html lang="en">
<head>
<meta charset="utf-8">
<title>Brightvale Imaging – Keep Your Precious Memories Forever</title>
<link href="https://fonts.googleapis.com/css2?family=Montserrat:wght@300;400;600;700;800&family=Kaushan+Script&display=swap" rel="stylesheet">
<style>
  :root {
    --ink: #1b1c1f;
    --night: #26282d;
    --night-deep: #17181b;
    --brand-blue: #4a78b0;
    --brand-blue-soft: #8fb0d6;
    --panel-blue: #5b85b8;
    --film-grey: #8e9096;
    --film-edge: #1a1b1e;
    --paper: #ffffff;
    --text: #222326;
  }
  * { box-sizing: border-box; margin: 0; padding: 0; }
  html, body { width: 750px; height: 1200px; overflow: hidden; background: var(--paper); }
  body { font-family: "Montserrat", Arial, sans-serif; color: var(--text); }

  .flyer { position: relative; width: 750px; height: 1200px; overflow: hidden; background: var(--paper); }
  .flyer__art { position: absolute; inset: 0; width: 750px; height: 1200px; }

  .headline { position: absolute; top: 70px; right: 48px; text-align: right; line-height: 1; }
  .headline__kicker { display: block; font-weight: 300; font-size: 27px; letter-spacing: 1px; color: #e9ebee; }
  .headline__accent { display: block; font-weight: 800; font-size: 68px; color: var(--brand-blue); letter-spacing: 1px; margin-top: 4px; }
  .headline__main { display: block; font-weight: 300; font-size: 74px; color: #ffffff; letter-spacing: 2px; margin-top: 2px; }

  .brand { position: absolute; left: 44px; top: 290px; color: #ffffff; }
  .brand__mark { width: 46px; height: 46px; border-radius: 50%; background: var(--brand-blue); margin: 0 0 14px 70px; }
  .brand__name { font-weight: 300; font-size: 33px; letter-spacing: 6px; }
  .brand__sub { display: flex; align-items: center; gap: 10px; margin-top: 6px; color: var(--brand-blue-soft); font-weight: 400; font-size: 15px; letter-spacing: 6px; }
  .brand__sub::before, .brand__sub::after { content: ""; height: 1px; width: 60px; background: var(--brand-blue-soft); }

  .service { position: absolute; width: 330px; }
  .service--scanning { left: 40px; top: 730px; }
  .service--digitising { left: 405px; top: 575px; }
  .service__title { display: flex; align-items: flex-start; gap: 10px; color: var(--brand-blue); line-height: 1; }
  .service__dot { flex: none; width: 20px; height: 20px; border-radius: 50%; background: var(--brand-blue); margin-top: 14px; }
  .service__strong { display: block; font-weight: 800; font-size: 25px; }
  .service__light { display: block; font-weight: 300; font-size: 25px; margin-top: 2px; }
  .service__lead { font-weight: 700; font-size: 13px; line-height: 1.35; color: var(--ink); margin: 12px 0 10px 30px; }
  .service__body { font-weight: 400; font-size: 11px; line-height: 1.45; color: var(--text); margin-left: 30px; }

  .divider { position: absolute; left: 385px; top: 590px; width: 1px; height: 240px; background: var(--brand-blue); }

  .contact { position: absolute; left: 30px; bottom: 22px; display: flex; align-items: center; gap: 10px; }
  .contact__name { font-family: "Kaushan Script", "Brush Script MT", cursive; font-size: 38px; color: var(--brand-blue); }
  .contact__icon { width: 30px; height: 30px; }
  .contact__phone { font-weight: 800; font-size: 34px; color: var(--ink); letter-spacing: -0.5px; }
  .website { position: absolute; right: 32px; bottom: 48px; font-weight: 700; font-size: 24px; color: var(--brand-blue); }
</style>
</head>
<body>
<main class="flyer">
  <svg class="flyer__art" viewBox="0 0 750 1200">
    <defs>
      <linearGradient id="nightScene" x1="0" y1="0" x2="1" y2="1">
        <stop offset="0" stop-color="#2e3036"/>
        <stop offset="1" stop-color="#17181b"/>
      </linearGradient>
      <linearGradient id="usbScene" x1="0" y1="0" x2="1" y2="1">
        <stop offset="0" stop-color="#a9c2df"/>
        <stop offset="1" stop-color="#5f88ba"/>
      </linearGradient>
    </defs>

    <rect class="hero-backdrop" x="0" y="0" width="750" height="760" fill="url(#nightScene)" role="img" aria-label="Dark photo of a vintage car"/>

    <path class="body-paper" d="M0 682 C160 682 260 595 390 522 S620 425 750 425 L750 1200 L0 1200 Z" fill="#ffffff"/>

    <g class="film-strip">
      <path d="M-20 620 C160 620 250 530 380 460 S620 360 770 365" fill="none" stroke="#b9bbc0" stroke-width="128"/>
      <path d="M-20 620 C160 620 250 530 380 460 S620 360 770 365" fill="none" stroke="var(--film-edge)" stroke-width="118"/>
      <path d="M-20 620 C160 620 250 530 380 460 S620 360 770 365" fill="none" stroke="var(--film-grey)" stroke-width="84"/>
      <g transform="translate(45 618) rotate(-2)"><rect x="-58" y="-36" width="116" height="72" rx="6" fill="#9a8a6c" role="img" aria-label="Photo of a cottage among trees"/></g>
      <g transform="translate(180 592) rotate(-14)"><rect x="-60" y="-36" width="120" height="72" rx="6" fill="#b8413f" role="img" aria-label="Photo of a child holding red autumn leaves"/></g>
      <g transform="translate(320 498) rotate(-32)"><rect x="-62" y="-36" width="124" height="72" rx="6" fill="#c99a5c" role="img" aria-label="Photo of a family sitting in a golden field"/></g>
      <g transform="translate(465 420) rotate(-24)"><rect x="-62" y="-36" width="124" height="72" rx="6" fill="#b8c2c9" role="img" aria-label="Photo of a wedding couple by the sea"/></g>
      <g transform="translate(615 374) rotate(-10)"><rect x="-62" y="-36" width="124" height="72" rx="6" fill="#4b4e55" role="img" aria-label="Photo of a vintage car"/></g>
      <g transform="translate(740 365)"><rect x="-55" y="-36" width="110" height="72" rx="6" fill="#5c5f66" role="img" aria-label="Photo of a street scene"/></g>
    </g>

    <polygon class="panel-blue" points="0,905 750,825 750,1080 0,1135" fill="var(--panel-blue)"/>
    <polygon class="usb-photo" points="0,905 375,865 375,1110 0,1135" fill="url(#usbScene)" role="img" aria-label="Photo of two blue and white USB drives"/>
    <rect class="slides-photo" x="398" y="880" width="160" height="195" fill="#8c3a36" role="img" aria-label="Photo of colourful photo slides in a pile"/>
    <rect class="boxes-photo" x="572" y="850" width="160" height="210" fill="#b98558" role="img" aria-label="Photo of wooden USB gift boxes"/>
  </svg>

  <h1 class="headline">
    <span class="headline__kicker">KEEP YOUR PRECIOUS</span>
    <span class="headline__accent">MEMORIES</span>
    <span class="headline__main">FOREVER</span>
  </h1>

  <div class="brand">
    <div class="brand__mark"></div>
    <div class="brand__name">BRIGHTVALE</div>
    <div class="brand__sub">IMAGING</div>
  </div>

  <section class="service service--digitising">
    <h2 class="service__title"><span class="service__dot"></span><span><span class="service__strong">SLIDES AND VHS</span><span class="service__light">DIGITISING</span></span></h2>
    <p class="service__lead">Conversion of VHS tapes to computer friendly video files using high quality broadcast equipment.</p>
    <p class="service__body">Your tapes will be personally picked up and returned to your home with a USB drive.</p>
  </section>

  <div class="divider"></div>

  <section class="service service--scanning">
    <h2 class="service__title"><span class="service__dot"></span><span><span class="service__strong">PHOTO NEGATIVE</span><span class="service__light">SCANNING</span></span></h2>
    <p class="service__lead">Digitising photo slides and negatives into crisp digital photos.</p>
    <p class="service__body">Your photos will be personally picked up and delivered back to your home with high resolution JPEG files on a USB drive</p>
  </section>

  <div class="contact">
    <span class="contact__name">Margot</span>
    <svg class="contact__icon" viewBox="0 0 30 30" aria-hidden="true">
      <circle cx="15" cy="15" r="14" fill="var(--brand-blue)"/>
      <path d="M10.5 8.5c1-.6 1.8-.4 2.3.6l1 2c.3.7.1 1.3-.5 1.8l-.8.6c.6 1.6 1.8 2.9 3.4 3.6l.6-.8c.5-.6 1.1-.8 1.8-.5l2 1c1 .5 1.2 1.3.6 2.3-.9 1.4-2.4 1.9-4 1.3-3.5-1.3-6.1-3.9-7.3-7.4-.5-1.6 0-3 .9-4.5z" fill="#fff"/>
    </svg>
    <span class="contact__phone">0478 219 836</span>
  </div>
  <div class="website">www.brightvale.com</div>
</main>
</body>
</html>
```